Statement on the current financial and economic crisis, with a focus on Greece,

Anybody can become angry - that is easy, but to be angry with the right person and to the right degree and at the right time and for the right purpose, and in the right way - that is not within everybody's power and is not easy.
(Thessidor ) greek philosopher

i want to do a poster with this words from Thessidor greek philosopher and to show this statement for the greek people... its about for my project that i am doing.
Updates

Target Market(s)

my audience will be greek people but not only, from 18-80 years old for that reason i want my statement to be in english.

Industry/Entity Type

Financial

Requirements
Must have
• Anybody can become angry - that is easy, but to be angry with the right person and to the right degree and at the right time and for the right purpose, and in the right way - that is not within everybody's power and is not easy.
i want to show in my poster this statement from:
Thessidor greek philosopher (384 – 322 BC)

```html
<!DOCTYPE html>
<html lang="en">
<head>
<meta charset="utf-8">
<title>Thessidor – On Anger</title>
<link rel="stylesheet" href="https://fonts.googleapis.com/css2?family=Stardos+Stencil:wght@700&display=swap">
<style>
  :root {
    --page: #ffffff;
    --card: #00bbe3;
    --ink: #ffffff;
    --edge: #8a8a8a;
  }
  html, body {
    margin: 0;
    padding: 0;
    overflow: hidden;
  }
  body {
    width: 1003px;
    height: 1200px;
    background: var(--page);
    position: relative;
    font-family: "Stardos Stencil", "Georgia", serif;
    font-weight: 700;
    color: var(--ink);
    box-shadow: inset 0 0 0 1px var(--edge);
  }
  .poster-card {
    position: absolute;
    left: 215px;
    top: 204px;
    width: 574px;
    height: 818px;
    background: var(--card);
    border-radius: 42px;
  }
  .quote-line,
  .author,
  .author-note {
    position: absolute;
    left: 0;
    width: 100%;
    text-align: center;
    white-space: nowrap;
    line-height: 1;
    transform: translateY(-50%);
    margin: 0;
  }
  .line-opening   { top: 151px; font-size: 48px; }
  .line-angry     { top: 208px; font-size: 37px; }
  .line-easy      { top: 258px; font-size: 37px; }
  .line-person    { top: 309px; font-size: 22px; }
  .line-degree    { top: 360px; font-size: 37px; letter-spacing: 0.5px; }
  .line-purpose   { top: 419px; font-size: 35px; }
  .line-way       { top: 483px; font-size: 35px; letter-spacing: 0.5px; }
  .line-power     { top: 540px; font-size: 22px; }
  .line-closing   { top: 595px; font-size: 33px; }
  .author         { top: 660px; font-size: 20px; }
  .author-note    { top: 681px; font-size: 9px; letter-spacing: 0.5px; }
</style>
</head>
<body>
  <main class="poster-card">
    <blockquote class="quote" style="margin:0">
      <p class="quote-line line-opening">Anybody</p>
      <p class="quote-line line-angry">can become angry -</p>
      <p class="quote-line line-easy">that is easy,</p>
      <p class="quote-line line-person">but to be angry with the right person</p>
      <p class="quote-line line-degree">and to the right degree</p>
      <p class="quote-line line-purpose">and at the right purpose,</p>
      <p class="quote-line line-way">and in the right way -</p>
      <p class="quote-line line-power">that is not within everybody's power</p>
      <p class="quote-line line-closing">and is not easy.</p>
    </blockquote>
    <p class="author">Thessidor</p>
    <p class="author-note">(greek philosopher)</p>
  </main>
</body>
</html>
```